Full redesign of dairy products including Yogurts and milk products

We have been selling milk and yogurts over the past 15 years, we are now expanding into a wider range of dairy products to include flavoured milk and a variety of soft cheeses such as cottage cheese etc. It is now the perfect time to redesign our existing product range to give a fresh and new look to our products. Have a look at our website https://rtvale.co.uk/ for further details. We are rebranding as NUVELKA, I have attached a identify pack to give you a feel of the the design, this is a fresh and bright design that will reflect the fresh and tasteful products we produce. The current milk label cut out is unique to us and I would like to continue using this shape which I have attached, the other labels should be done using regular rectangular rounded edge labels. The following designs are required;
1 x Universal lid (71.5mm) design for all below 120ml Yogurts
-11 x 120 ml Yogurt pot designs
Strawberry
Strawberry Banana
Peach & Apricot
Cherry
Toffee
Vanilla
Natural
Orange
Forest Fruits
Pineapple
Mango
1 x Universal lid (95.5mm)for below yogurts (can be identical to the 120ml Lid)
-4 x 450ml Yogurt Pots
Strawberry
Natural
Toffee
Mango
-1 x Universal (95.5mm) LID for 150ml Greek Yogurt
-4 x Designs for 150ml Greek yogurt POT
Strawberry
Natural
Vanilla
Mango

3 x Flavoured milk labels 2 sizes 250ml & 1lt
Biscotti
Chocolate
Strawberry

Cottage Cheese Lid & Pot 250g

1 x Quark universal Lid (95.5mm)
4 x Quark 250g pots
Natural
Strawberry
Peach & Apricot
Mango

```html
<!DOCTYPE html>
<html lang="en">
<head>
<meta charset="UTF-8">
<title>NUVELKA Strawberry Yogurt Pot Label</title>
<link href="https://fonts.googleapis.com/css2?family=Sniglet:wght@400;800&family=Nunito:wght@700;800&display=swap" rel="stylesheet">
<style>
  :root {
    --backdrop: #8db488;
    --pot-red: #c4161c;
    --pot-red-light: #e1444a;
    --cream: #ffffff;
    --brand-green: #3f9a3c;
    --splash-light: #f1f2f4;
    --splash-mid: #c9ccd2;
  }
  * { box-sizing: border-box; margin: 0; padding: 0; }
  html, body {
    width: 1200px; height: 900px; overflow: hidden;
    background: var(--backdrop);
  }
  .canvas { position: relative; width: 1200px; height: 900px; }
  .pot-label {
    position: absolute; left: 444px; top: 222px;
    width: 327px; height: 466px;
    border-radius: 14px; overflow: hidden;
    background: linear-gradient(90deg, var(--pot-red-light) 0%, var(--pot-red) 35%, var(--pot-red) 70%, var(--pot-red-light) 100%);
  }
  .cream-band {
    position: absolute; left: 0; top: 0; width: 100%; height: 100px;
    background: var(--cream);
  }
  .drip-art {
    position: absolute; left: 0; top: 100px; width: 100%; height: 58px;
    background: linear-gradient(180deg, rgba(255,255,255,0.85) 0%, rgba(255,255,255,0.35) 55%, rgba(255,255,255,0) 100%);
  }
  .brand-name {
    position: absolute; top: 56px; left: 0; width: 100%;
    text-align: center;
    font-family: "Sniglet", sans-serif; font-weight: 800;
    font-size: 26px; line-height: 1; letter-spacing: 1px;
    color: var(--brand-green);
  }
  .product-title {
    position: absolute; top: 168px; left: 0; width: 100%;
    text-align: center;
    font-family: "Sniglet", sans-serif; font-weight: 400;
    font-size: 72px; line-height: 1;
    color: var(--cream);
  }
  .hero-art {
    position: absolute; left: 54px; top: 258px;
    width: 192px; height: 132px;
    border-radius: 50%;
    background: radial-gradient(ellipse at 50% 55%, var(--splash-light) 0%, var(--splash-mid) 55%, rgba(211,35,44,0.6) 100%);
  }
  .flavour-name {
    position: absolute; top: 404px; left: 0; width: 100%;
    text-align: center;
    font-family: "Nunito", sans-serif; font-weight: 800;
    font-size: 16px; line-height: 1; letter-spacing: 1.5px;
    color: var(--cream);
  }
  .net-weight {
    position: absolute; top: 437px; right: 38px;
    font-family: "Nunito", sans-serif; font-weight: 700;
    font-size: 7px; line-height: 1; color: var(--cream);
  }
  .net-weight strong { font-size: 10px; }
</style>
</head>
<body>
<main class="canvas">
  <section class="pot-label">
    <div class="cream-band"></div>
    <div class="drip-art" role="img" aria-label="White yogurt dripping down from the top band"></div>
    <div class="brand-name">NUVELKA</div>
    <h1 class="product-title">Yogurt</h1>
    <div class="hero-art" role="img" aria-label="Milk splash with fresh strawberries and leaves"></div>
    <p class="flavour-name">STRAWBERRY</p>
    <p class="net-weight">Net. Wt:<strong>500g</strong></p>
  </section>
</main>
</body>
</html>
```